Luxury Brand Vision Deck (Canva) | Coffee Table Book Style

I am looking for a designer to create a luxury, editorial-style pitch deck for a high-end hospitality brand (restaurants + lifestyle).

This deck must feel like a coffee table book, not a corporate presentation.

Non-Negotiable Requirements:
Must be designed in Canva
Clean, minimal, luxury aesthetic
Editorial / fashion-magazine inspired
Spacious layouts, strong typography
Designed to be reused as a template

Visual Style:
Black, white, cream, charcoal, soft neutrals
No bright colors
No gradients
No busy backgrounds
Elegant, modern fonts
Image-forward pages

Use Case:
Digital pitch deck
Later printed as a physical coffee table booklet
Reused for future meetings and brand presentations

I Will Provide:
All written content (slide-by-slide)
Brand context and inspiration
Image direction or assets

You Are a Good Fit If:
You love minimal, luxury design
You understand editorial layout and spacing
You have strong attention to detail
You enjoy premium branding projects
This project is about restraint, confidence, and elevated simplicity.

https://www.linkedin.com/company/lumo-by-the-bay/

https://www.lumobythebay.example/

Target Market(s)

Luxury hospitality / restaurant group leadership (owners, founders, executives)

Industry/Entity Type

Hospitality, Restaurants, Luxury Lifestyle Brand

Requirements
Must have
• Must be designed in Canva

```html
<!DOCTYPE html>
<html lang="en">
<head>
<meta charset="utf-8">
<title>Lumo Group — A Marketing Vision</title>
<link href="https://fonts.googleapis.com/css2?family=Cinzel:wght@600;700&family=Cormorant+Garamond:wght@300;400&family=Lato:wght@300;400&display=swap" rel="stylesheet">
<style>
  :root {
    --page: #ffffff;
    --cream: #f6f5f0;
    --ink: #2b2a28;
    --body: #7a7873;
    --muted: #8d8b86;
  }
  * { margin: 0; padding: 0; box-sizing: border-box; }
  html, body { width: 1200px; height: 1200px; overflow: hidden; background: var(--page); }
  .canvas { position: relative; width: 1200px; height: 1200px; }
  .slide { position: absolute; width: 482px; height: 272px; background: var(--cream); overflow: hidden; }
  .s1 { left: 98px; top: 121px; }
  .s2 { left: 631px; top: 121px; }
  .s3 { left: 96px; top: 468px; }
  .s4 { left: 630px; top: 468px; }
  .s5 { left: 96px; top: 815px; }
  .s6 { left: 631px; top: 815px; }

  .heading {
    position: absolute;
    font-family: 'Cinzel', serif;
    font-weight: 700;
    font-size: 11.5px;
    line-height: 12.6px;
    letter-spacing: 0.17em;
    color: var(--ink);
  }
  .copy {
    position: absolute;
    font-family: 'Lato', sans-serif;
    font-weight: 400;
    font-size: 5.3px;
    line-height: 8.6px;
    letter-spacing: 0.02em;
    color: var(--body);
  }
  .copy p { margin-bottom: 8.6px; }
  .copy ul { list-style: none; margin: 0 0 8.6px 5px; }
  .copy li::before { content: "• "; }

  /* cover */
  .cover-title {
    position: absolute; left: 0; width: 100%; top: 99px; text-align: center;
    font-family: 'Cormorant Garamond', serif; font-weight: 300;
    font-size: 33px; line-height: 32px; letter-spacing: 0.12em; color: var(--ink);
  }
  .cover-sub {
    position: absolute; left: 0; width: 100%; top: 130px; text-align: center;
    font-family: 'Lato', sans-serif; font-weight: 300;
    font-size: 17px; line-height: 20px; letter-spacing: 0.2em; color: var(--ink);
  }
  .cover-line {
    position: absolute; left: 128px; width: 226px; top: 154px; text-align: center;
    font-family: 'Lato', sans-serif; font-size: 4.3px; line-height: 6.4px;
    letter-spacing: 0.42em; color: var(--muted);
  }
  .cover-credit {
    position: absolute; left: 0; width: 100%; top: 244px; text-align: center;
    font-family: 'Lato', sans-serif; font-size: 3.6px; line-height: 4.6px;
    letter-spacing: 0.3em; color: var(--muted);
  }

  .photo {
    position: absolute; left: 0; top: 0; width: 131px; height: 272px;
    background: linear-gradient(180deg, #a8683a 0%, #6b3a26 38%, #2a2040 70%, #14132a 100%);
  }

  .rating { position: absolute; left: 298px; display: flex; align-items: center; gap: 4px; }
  .rating svg { width: 14px; height: 14px; }
  .rating .value { font-family: 'Cormorant Garamond', serif; font-weight: 400; font-size: 11px; letter-spacing: 0.08em; color: var(--ink); margin-left: 2px; }
  .rating-now { top: 104px; }
  .rating-goal { top: 141px; }
  .progress { position: absolute; left: 297px; top: 131px; width: 116px; height: 6px; }
</style>
</head>
<body>
<svg width="0" height="0" style="position:absolute">
  <defs>
    <symbol id="star" viewBox="0 0 24 24">
      <polygon points="12,1.5 15,9 23,9.3 16.8,14.3 19,22.3 12,17.8 5,22.3 7.2,14.3 1,9.3 9,9"/>
    </symbol>
  </defs>
</svg>
<main class="canvas">

  <section class="slide s1">
    <h1 class="cover-title">LUMO GROUP</h1>
    <div class="cover-sub">A Marketing Vision</div>
    <div class="cover-line">HOW I SEE THE BRAND, WHERE I BELIEVE IT CAN GO, AND HOW I WOULD HELP TAKE IT THERE.</div>
    <div class="cover-credit">Celeste Marlowe<br>Director of Marketing Candidate</div>
  </section>

  <section class="slide s2">
    <h2 class="heading" style="left:26px; top:56px;">WHY LUMO IS DIFFERENT</h2>
    <div class="copy" style="left:26px; top:82px; width:218px;">
      <p>Lumo Group isn't just a collection of restaurants. It's an energy. A mood. A place people want to be part of.</p>
      <p>Over the past year and a half, I've been deeply immersed in the Lumo ecosystem as a client, a collaborator, and a genuine fan of the brand. I've seen firsthand what makes these concepts special: the atmosphere, the people, the confidence, and the way guests feel both when they walk in and when they leave.</p>
      <p>What excites me most is that Lumo already has the hard part. The energy is real, and people feel it the moment they step into the space.</p>
      <p>The opportunity now is about refining and protecting that magic as the brand continues to grow. Making sure what guests experience in the room, what they see online, and what they hear about Lumo all tell the same elevated story, wherever they encounter the brand.</p>
    </div>
  </section>

  <section class="slide s3">
    <h2 class="heading" style="left:26px; top:73px;">THREE PILLARS<br>I COMEBACK TO<br>EVERY TIME</h2>
    <div class="copy" style="left:26px; top:124px; width:222px;">
      <p>When I think about taking a hospitality brand to the next level, I always return to three things:</p>
      <ul>
        <li>Reputation that reflects reality</li>
        <li>Identity that lives beyond the walls</li>
        <li>Details that quietly elevate everything</li>
      </ul>
      <p>These pillars guide how I prioritize, what I push forward first, and how I think about long-term brand equity rather than short-term noise.</p>
    </div>
  </section>

  <section class="slide s4">
    <div class="photo" role="img" aria-label="Photo: guests celebrating under woven pendant lamps with falling gold confetti"></div>
    <h2 class="heading" style="left:167px; top:51px;">A BRAND READY<br>FOR ITS NEXT ERA</h2>
    <div class="copy" style="left:167px; top:94px; width:284px;">
      <p>Lumo already has what most brands spend years trying to manufacture. Energy.</p>
      <p>Identity. A loyal following. Cultural relevance.</p>
      <p>The restaurants are known. The rooms are full. The brand is respected. And this is often the exact moment where hospitality groups either plateau as an "it" spot or intentionally evolve into something bigger.</p>
      <p>The next chapter is not about awareness. It's about elevation.</p>
      <p>Elevation looks like tighter alignment between what people hear, what they see online, and what they experience in person. It looks like consistency across concepts without losing individuality. It looks like turning momentum into something scalable and durable.</p>
      <p>This is the stage Lumo is in now. And this is the work I'm genuinely excited to do.</p>
    </div>
  </section>

  <section class="slide s5">
    <h2 class="heading" style="left:27px; top:75px;">PRIORITY ONE:<br>REVIEWS &amp; REPUTATION</h2>
    <div class="copy" style="left:27px; top:113px; width:224px;">
      <p>Findr is often the final decision point. Even when someone hears about a restaurant through friends, social media, or word of mouth.</p>
      <p>A guest can be already excited to go, then do a quick search, see a 3.8 rating, and quietly choose a different restaurant. That friction is real, and it happens every day, especially in a market like Miami where guests have endless options.</p>
      <p>Lumo, Sahra, and Marisol are high-quality, high-demand concepts. The current ratings don't reflect that reality. Which means the online reputation is likely costing the group first-time visits without anyone inside the business fully seeing the loss.</p>
    </div>
    <div class="rating rating-now" aria-label="Current rating 3.8">
      <svg fill="var(--ink)"><use href="#star"/></svg>
      <svg fill="var(--ink)"><use href="#star"/></svg>
      <svg fill="var(--ink)"><use href="#star"/></svg>
      <svg fill="var(--ink)"><use href="#star"/></svg>
      <svg fill="none" stroke="var(--ink)" stroke-width="1.6"><use href="#star"/></svg>
      <span class="value">3.8</span>
    </div>
    <svg class="progress" viewBox="0 0 116 6" aria-hidden="true">
      <line x1="0" y1="3" x2="113" y2="3" stroke="var(--ink)" stroke-width="0.9"/>
      <polyline points="110,1 114,3 110,5" fill="none" stroke="var(--ink)" stroke-width="0.9"/>
    </svg>
    <div class="rating rating-goal" aria-label="Target rating 4.5 plus">
      <svg fill="var(--ink)"><use href="#star"/></svg>
      <svg fill="var(--ink)"><use href="#star"/></svg>
      <svg fill="var(--ink)"><use href="#star"/></svg>
      <svg fill="var(--ink)"><use href="#star"/></svg>
      <svg fill="var(--ink)"><use href="#star"/></svg>
      <span class="value">4.5+</span>
    </div>
  </section>

  <section class="slide s6">
    <h2 class="heading" style="left:27px; top:58px;">HOW I'D LIFT RATINGS<br>AUTHENTICALLY</h2>
    <div class="copy" style="left:27px; top:97px; width:222px;">
      <p style="margin-bottom:13px;">Improving reviews isn't about asking harder. It's about building a system that makes it easy for happy guests to speak up.</p>
      <p>My approach would focus on:</p>
      <ul>
        <li>Natural, staff-aligned prompts that feel guest-first</li>
        <li>Post-visit follow-ups designed to capture satisfied diners</li>
        <li>Thoughtful incentives that feel elevated and on-brand</li>
        <li>Tracking progress monthly and treating reviews as a true brand health metric</li>
        <li>A simple internal rhythm: monitor, respond, refine, repeat</li>
      </ul>
      <p>The goal is not just a higher number. It's alignment between the real-life experience and what the world sees online.</p>
    </div>
  </section>

</main>
</body>
</html>
```